Dr Fobu smart screen Flyer design

Hi,

Please see attached file as I have done up a very very basic flyer just with the information that will need to be presented.

Please don't go with this as a format I would like, as I have no design skills at all.

I'm looking for something that is basic but professional looking capturing this information.
I would prefer if the symbols were changed so they were all consistent and the colour scheme worked together with the logo.

If you can use the picture of the screen provided as I will replace this once my product has its photoshoot.

Thanks!

```html
<!DOCTYPE html>
<html lang="en">
<head>
<meta charset="utf-8">
<title>Dr Fobu Smart Screen Flyer</title>
<link rel="stylesheet" href="https://fonts.googleapis.com/css2?family=Montserrat:wght@400;600;700&family=Oswald:wght@400;500;700&display=swap">
<style>
  :root {
    --page-bg: #e9e6e2;
    --ink: #111111;
    --band: #0d0d0d;
    --cyan: #3fc1e9;
    --yellow: #fde30a;
    --magenta: #b8449b;
    --white: #ffffff;
    --text: #1d1d1d;
    --sky-a: #e4f0fb;
    --sky-b: #f3e6f6;
    --pink: #f4c6ec;
  }
  * { box-sizing: border-box; margin: 0; padding: 0; }
  html, body { width: 1200px; height: 1200px; overflow: hidden; background: var(--page-bg); }
  .flyer {
    position: absolute; left: 194px; top: 30px;
    width: 950px; height: 1335px;
    transform: scale(0.854); transform-origin: 0 0;
    background: var(--white); overflow: hidden;
    font-family: "Montserrat", sans-serif; color: var(--text);
    box-shadow: 0 6px 24px rgba(0,0,0,0.18);
  }
  .masthead {
    position: absolute; left: 0; top: 0; width: 950px; height: 292px;
    background: linear-gradient(100deg, var(--sky-a) 0%, #eef2fb 45%, var(--sky-b) 75%, var(--pink) 100%);
  }
  .brand {
    position: absolute; left: 95px; top: 120px;
    display: flex; align-items: center; gap: 18px;
    font-family: "Montserrat", sans-serif; font-weight: 600; font-size: 64px;
    color: var(--ink); letter-spacing: 2px;
  }
  .brand-mark { width: 30px; height: 30px; background: var(--ink); }
  .hero-photo {
    position: absolute; left: 540px; top: 35px; width: 320px; height: 350px;
    background: linear-gradient(180deg, #6fa7d8 0%, #9cc7e6 28%, #6fae3c 55%, #4e8f22 100%);
    box-shadow: 18px 0 0 #141414;
  }
  .feature-band {
    position: absolute; left: 0; top: 292px; width: 950px; height: 410px;
    background: var(--band); text-align: center;
  }
  .headline { font-family: "Oswald", sans-serif; color: var(--cyan); font-weight: 400; line-height: 1; }
  .headline-top { position: absolute; left: 0; width: 100%; top: 70px; font-size: 52px; }
  .headline-mid { position: absolute; left: 0; width: 100%; top: 126px; font-size: 54px; }
  .headline-main {
    position: absolute; left: 0; width: 100%; top: 178px;
    font-family: "Oswald", sans-serif; font-weight: 700; font-size: 118px;
    color: var(--yellow); line-height: 1; letter-spacing: 1px;
  }
  .intro {
    position: absolute; left: 0; width: 100%; top: 292px;
    color: var(--white); font-size: 18.5px; line-height: 28px;
  }
  .feature {
    position: absolute; width: 290px; text-align: center;
  }
  .feature svg { display: block; margin: 0 auto; height: 92px; width: 100px; }
  .feature h3 { margin-top: 26px; color: var(--cyan); font-size: 18px; font-weight: 700; }
  .feature p { margin-top: 8px; font-size: 15.5px; line-height: 19px; color: var(--text); }
  .row-1 { top: 755px; }
  .row-2 { top: 1008px; }
  .col-1 { left: 22px; }
  .col-2 { left: 330px; }
  .col-3 { left: 638px; }
  .quote { position: absolute; left: 648px; top: 1060px; width: 302px; height: 200px; }
  .quote-text {
    position: absolute; left: 672px; top: 1100px; width: 270px;
    font-family: "Oswald", sans-serif; font-weight: 500; color: var(--white); line-height: 1.05;
    transform: rotate(-3deg);
  }
  .quote-text .phone { display: block; font-size: 46px; }
  .quote-text .cta { display: block; font-size: 36px; }
  .footer { position: absolute; left: 0; top: 1272px; width: 950px; height: 63px; }
  .contact {
    position: absolute; top: 1296px; display: flex; align-items: center; gap: 14px;
    color: var(--white); font-size: 16px;
  }
  .contact svg { width: 28px; height: 22px; }
  .contact-email { left: 57px; }
  .contact-web { left: 405px; }
</style>
</head>
<body>
<div class="flyer">
  <header class="masthead">
    <div class="brand"><span class="brand-mark"></span>Dr Fobu</div>
  </header>
  <div class="hero-photo" role="img" aria-label="Outdoor LED screen showing children running across a green field"></div>

  <section class="feature-band">
    <h2 class="headline headline-top">BRING ATTNETION</h2>
    <h2 class="headline headline-mid">TO YOUR BUSSINESS WITH YOUR OWN</h2>
    <h1 class="headline-main">HD LED DISPLAY</h1>
    <p class="intro">Our displays can be mounted outdoors on walls,roofs, fixed signs, trailer mounted ect.<br>
      We also do indoor led screens for shop fronts and display stands.<br>
      All screens are cumtom built to your requirements including size, shape and even curved</p>
  </section>

  <div class="feature row-1 col-1">
    <svg viewBox="0 0 100 92" fill="none" stroke="var(--cyan)" stroke-width="7">
      <path d="M10 50 V70 H28 M24 50 V88" />
      <path d="M58 56 H40 V88 H58 V72 H48" />
      <path d="M52 36 A20 20 0 0 1 72 56" /><path d="M52 20 A36 36 0 0 1 88 56" /><path d="M52 4 A52 52 0 0 1 98 50" />
    </svg>
    <h3>4G Capable</h3>
    <p>Change screen content with a click<br>of the mouse anywhere in the</p>
  </div>
  <div class="feature row-1 col-2">
    <svg viewBox="0 0 100 92" fill="none" stroke="var(--cyan)" stroke-width="6" stroke-linecap="round">
      <circle cx="50" cy="46" r="22" />
      <path d="M50 30 A16 16 0 0 0 50 62 Z" fill="var(--cyan)" stroke="none" />
      <path d="M50 4 V12 M50 80 V88 M8 46 H16 M84 46 H92 M20 16 L26 22 M74 70 L80 76 M80 16 L74 22 M26 70 L20 76" />
    </svg>
    <h3>Inteligent brightness control</h3>
    <p>Screen will automatically adjust suit ambiant light improveing sreen veiwing quality and saving in power consumption</p>
  </div>
  <div class="feature row-1 col-3">
    <svg viewBox="0 0 100 92" fill="var(--cyan)">
      <path d="M28 40 L22 18 L38 28 L50 8 L62 28 L78 18 L72 40 Z" />
      <circle cx="22" cy="16" r="4" /><circle cx="50" cy="6" r="4" /><circle cx="78" cy="16" r="4" />
      <path d="M26 46 H74 L84 60 L50 92 L16 60 Z" />
    </svg>
    <h3>High quality products</h3>
    <p>Setting high standard for color, brightness and sharpness these LED modules will create attention.</p>
  </div>
  <div class="feature row-2 col-1">
    <svg viewBox="0 0 100 92" fill="none" stroke="var(--cyan)" stroke-width="8" stroke-linecap="round">
      <path d="M12 36 A54 54 0 0 1 88 36" /><path d="M26 52 A34 34 0 0 1 74 52" />
      <circle cx="50" cy="74" r="7" fill="var(--cyan)" stroke="none" />
    </svg>
    <h3>Wifi Capable</h3>
    <p>Change screen content with a PC,<br>table or mobile phone with an<br>easy to use app</p>
  </div>
  <div class="feature row-2 col-2">
    <svg viewBox="0 0 100 92" fill="none" stroke="var(--cyan)" stroke-width="5">
      <rect x="16" y="12" width="68" height="52" rx="3" />
      <path d="M6 72 H94 L88 80 H12 Z" fill="var(--cyan)" />
      <path d="M30 52 V40 M40 52 V30 M50 52 V36 M60 52 V26" stroke-width="6" />
      <path d="M66 30 L76 36 L70 38 L72 44" stroke-width="3" />
    </svg>
    <h3>Online Monitoring</h3>
    <p>Monitor cabinet temperature and humidity plus more in real time online.<br>Recive alerts via emial.</p>
  </div>

  <svg class="quote" viewBox="0 0 302 200">
    <polygon points="210,160 302,135 302,172" fill="#1a1a1a" />
    <polygon points="0,12 302,50 302,150 0,185" fill="var(--magenta)" />
  </svg>
  <div class="quote-text"><span class="phone">1300 DRFOBU</span><span class="cta">FOR A FREE QUOTE</span></div>

  <svg class="footer" viewBox="0 0 950 63">
    <polygon points="0,0 652,0 715,63 0,63" fill="var(--band)" />
    <polygon points="680,18 950,18 950,28 690,28" fill="var(--cyan)" />
    <polygon points="700,38 950,38 950,63 722,63" fill="var(--cyan)" />
  </svg>
  <div class="contact contact-email">
    <svg viewBox="0 0 28 22" fill="none" stroke="var(--white)" stroke-width="2"><rect x="1" y="2" width="26" height="18" /><path d="M1 2 L14 13 L27 2 M1 20 L11 11 M27 20 L17 11" /></svg>
    info@drfobu.com.au
  </div>
  <div class="contact contact-web">
    <svg viewBox="0 0 22 22" fill="none" stroke="var(--white)" stroke-width="2"><circle cx="11" cy="11" r="9.5" /><ellipse cx="11" cy="11" rx="4" ry="9.5" /><path d="M1.5 11 H20.5 M3 6 H19 M3 16 H19" /></svg>
    www.drfobu.com.au
  </div>
</div>
</body>
</html>
```